New Web Design Project (Blog, Video Blog and Education)

I have a domain www.brightlatticehub.tv I am looking for a website to post blogs and develop a site like https://tinkerandventure.com/ initially blogs then moving into video podcasting as we gain traction. The idea of www.brightlatticehub.tv is that it is about the connection to people, businesses and ideas that change the world.

Target Market(s)

This is a Blog, Podcast site with training material on it targeted at people who want access to connections and simple information on topics they are interested in.

Coding

Coded - Design and coding required

Number of Pages Required

4 page

Font styles to use
Other font styles liked:
• century gothic

Colors
ec1f27
5c5c5c
ffffff

Requirements
Must have
• Really good usability and A nice clean design that looks simple professional and compelling look at, not too busy and clear obvious navigation.
Nice to have
• Magical attraction to visitors.
Should not have
• Clunky design or poor usability

```html
<!DOCTYPE html>
<html lang="en">
<head>
<meta charset="utf-8">
<title>Bright Lattice Hub — Change the World</title>
<link rel="stylesheet" href="https://fonts.googleapis.com/css2?family=Questrial&family=Open+Sans:ital,wght@0,400;0,600;0,700;1,400&display=swap">
<style>
:root{
  --red:#ec1f27;
  --grey:#5c5c5c;
  --white:#ffffff;
  --ink:#1e1e1e;
  --soft:#f5f5f5;
  --line:#cfcfcf;
}
*{box-sizing:border-box;margin:0;padding:0}
html,body{width:1200px;height:4225px;overflow:hidden;background:var(--white)}
body{position:relative;font-family:"Open Sans",Arial,sans-serif;color:var(--ink)}
.abs{position:absolute}
.display{font-family:"Questrial","Century Gothic",sans-serif}

/* hero */
.hero{left:0;top:0;width:1200px;height:710px;
  background:radial-gradient(ellipse at 55% 40%,#4a3a3e 0%,#2a2530 35%,#15141c 70%,#0b0b10 100%)}
.brand{left:40px;top:30px;display:flex;align-items:center;gap:14px;color:var(--white);font-family:"Questrial",sans-serif;font-size:24px}
.brand-dot{width:22px;height:22px;border-radius:50%;background:var(--white)}
.nav{right:60px;top:42px;display:flex;gap:28px;align-items:center;font-family:"Questrial",sans-serif;font-size:16px;color:var(--white);letter-spacing:.5px}
.hero-arrow{top:340px;width:30px;height:30px}
.hero-title{left:0;top:382px;width:1200px;text-align:center;color:var(--white);font-size:84px;letter-spacing:1px;font-weight:700;font-family:"Questrial",sans-serif}
.hero-sub{left:0;top:488px;width:1200px;text-align:center;color:var(--white);font-size:23px;font-family:"Questrial",sans-serif}
.signup{left:282px;top:552px;width:636px;height:54px;display:flex}
.signup-field{flex:1;background:var(--white);display:flex;align-items:center;gap:10px;padding-left:24px;font-size:15px;color:#333}
.signup-go{width:62px;background:var(--red);color:var(--white);display:flex;align-items:center;justify-content:center;font-weight:700;font-size:16px}

/* featured */
.section-title{left:0;width:1200px;text-align:center;font-size:40px;color:var(--ink);font-family:"Questrial",sans-serif}
.partner{top:896px;width:180px;height:90px;border:2px solid var(--line);background:var(--white);display:flex;align-items:center;justify-content:center}
.partner span{display:block;width:120px;height:26px;background:#c9c9c9;border-radius:3px}
.side-arrow{width:34px;height:34px}

.pillar{top:1076px;height:270px}
.pillar-label{top:1375px;width:381px;text-align:center;font-size:35px;font-family:"Questrial",sans-serif}

/* blog */
.blog-band{left:0;top:1535px;width:1200px;height:1395px;background:var(--soft)}
.post-img{left:113px;width:405px;height:302px}
.post-title{left:572px;width:520px;font-size:24px;line-height:38px;font-family:"Questrial",sans-serif;color:#222}
.meta{display:flex;align-items:center;gap:8px;font-size:13px;color:#333}
.meta .sep{margin:0 4px}
.post-meta{left:572px}
.post-text{left:572px;width:520px;font-size:13px;line-height:28px;color:var(--grey)}
.read-more{left:572px;width:124px;height:40px;border:2px solid var(--red);border-radius:20px;color:var(--red);font-size:13px;font-weight:700;display:flex;align-items:center;justify-content:center}
.view-more{left:507px;top:2792px;width:172px;height:54px;border-radius:27px;background:var(--red);color:var(--white);font-weight:700;font-size:15px;display:flex;align-items:center;justify-content:center}

/* podcast */
.cast-img{top:3116px;width:310px;height:219px;background:linear-gradient(135deg,#3a3a42,#6e625c 55%,#2a2a30)}
.play{left:128px;top:83px;width:54px;height:54px;border-radius:50%;background:var(--white);display:flex;align-items:center;justify-content:center}
.cast-title{top:3352px;width:310px;font-size:17px;line-height:30px;font-weight:600;color:#222}
.cast-meta{top:3432px}
.round-arrow{top:3205px;width:40px;height:40px;border-radius:50%;border:2px solid #999;display:flex;align-items:center;justify-content:center;background:var(--white)}

/* quote */
.quote-band{left:0;top:3569px;width:1200px;height:310px;background:var(--red)}
.quote-badge{left:535px;top:3530px;width:130px;height:130px;border-radius:50%;background:var(--white);display:flex;align-items:center;justify-content:center}
.quote-text{left:150px;top:3680px;width:900px;text-align:center;color:var(--white);font-style:italic;font-size:26px;line-height:46px}
.quote-name{left:0;top:3790px;width:1200px;text-align:center;color:var(--white);font-weight:700;font-size:16px;letter-spacing:.5px}

/* footer */
.social{top:3984px;width:50px;height:50px;border:2px solid var(--red);border-radius:50%}
.contact{left:0;top:4068px;width:1200px;display:flex;justify-content:center;align-items:center;gap:10px;font-size:14px;color:#333}
.links{left:0;top:4117px;width:1200px;text-align:center;font-size:14px;color:#333;word-spacing:2px}
.links .bar{margin:0 14px}
.copyright{left:0;top:4162px;width:1200px;text-align:center;font-size:14px;color:#333}
</style>
</head>
<body>

<!-- hero -->
<div class="abs hero" role="img" aria-label="Photograph of a woman with glasses against a night city skyline with glowing connection lines"></div>
<div class="abs brand"><span class="brand-dot"></span>Bright Lattice Hub</div>
<nav class="abs nav">
  <span>PODCAST</span><span>BLOG</span><span>RESOURCES</span><span>BOOK</span><span>SPONSORS</span><span>CONTACT</span>
  <svg width="18" height="18" viewBox="0 0 18 18"><circle cx="7.5" cy="7.5" r="5.5" fill="none" stroke="#fff" stroke-width="2.4"/><line x1="11.5" y1="11.5" x2="16.5" y2="16.5" stroke="#fff" stroke-width="2.6"/></svg>
</nav>
<svg class="abs hero-arrow" style="left:38px" viewBox="0 0 30 30"><polyline points="20,4 9,15 20,26" fill="none" stroke="#fff" stroke-width="4"/></svg>
<svg class="abs hero-arrow" style="left:1130px" viewBox="0 0 30 30"><polyline points="10,4 21,15 10,26" fill="none" stroke="#fff" stroke-width="4"/></svg>
<h1 class="abs hero-title">CHANGE THE WORLD</h1>
<p class="abs hero-sub">Connection to people, businesses and ideas that change the world.</p>
<form class="abs signup">
  <div class="signup-field">
    <svg width="16" height="12" viewBox="0 0 16 12"><rect x="0" y="0" width="16" height="12" fill="#333"/><polyline points="0,0 8,7 16,0" fill="none" stroke="#fff" stroke-width="1.4"/></svg>
    Email Address
  </div>
  <div class="signup-go">GO</div>
</form>

<!-- featured -->
<h2 class="abs section-title" style="top:798px">AS FEATURED IN</h2>
<svg class="abs side-arrow" style="left:40px;top:924px" viewBox="0 0 34 34"><polyline points="22,5 10,17 22,29" fill="none" stroke="#666" stroke-width="3.5"/></svg>
<svg class="abs side-arrow" style="left:1130px;top:924px" viewBox="0 0 34 34"><polyline points="12,5 24,17 12,29" fill="none" stroke="#666" stroke-width="3.5"/></svg>
<div class="abs partner" style="left:113px"><span></span></div>
<div class="abs partner" style="left:311px"><span></span></div>
<div class="abs partner" style="left:510px"><span></span></div>
<div class="abs partner" style="left:708px"><span></span></div>
<div class="abs partner" style="left:907px"><span></span></div>

<div class="abs pillar" style="left:17px;width:380px;background:linear-gradient(135deg,#6b4a34,#a8805f 50%,#5a3b28)" role="img" aria-label="Photograph of clasped hands on a wooden table"></div>
<div class="abs pillar" style="left:411px;width:381px;background:radial-gradient(circle at 50% 50%,#b9c6d2 0%,#3d4a5c 35%,#101822 80%)" role="img" aria-label="Photograph of a glowing idea in an open hand with floating icons"></div>
<div class="abs pillar" style="left:803px;width:383px;background:linear-gradient(135deg,#8a5a34,#c08a5a 50%,#7a4c2a)" role="img" aria-label="Photograph of business people assembling puzzle pieces on a table"></div>
<div class="abs pillar-label" style="left:17px">PEOPLE</div>
<div class="abs pillar-label" style="left:411px">IDEAS</div>
<div class="abs pillar-label" style="left:804px">BUSINESS</div>

<!-- blog -->
<div class="abs blog-band"></div>
<h2 class="abs section-title" style="top:1612px">LATEST BLOG</h2>

<div class="abs post-img" style="top:1727px;background:linear-gradient(135deg,#3e4246,#8a8e90 50%,#2e3236)" role="img" aria-label="Photograph of a team joining puzzle pieces from above"></div>
<h3 class="abs post-title" style="top:1722px">Sed ut perspiciatis unde omnis iste natus sit vieol uptatem accusantium dolorem</h3>
<div class="abs meta post-meta" style="top:1816px">
  <svg width="13" height="13" viewBox="0 0 13 13"><rect x="0.5" y="1.5" width="12" height="11" fill="none" stroke="#ec1f27" stroke-width="1.4"/><rect x="0.5" y="1.5" width="12" height="3" fill="#ec1f27"/></svg>18/03/2019<span class="sep">|</span>
  <svg width="12" height="13" viewBox="0 0 12 13"><circle cx="6" cy="3.5" r="3" fill="#ec1f27"/><path d="M0 13 Q0 7 6 7 Q12 7 12 13Z" fill="#ec1f27"/></svg>John Doe
</div>
<p class="abs post-text" style="top:1858px">Nemo enim ipsam voluptatem quia voluptas sit aspernatur aut odit aut fugit, sed quia consequuntur magni dolores eos qui ratione voluptatem sequi nesciuntu po rro quisquam est, qui dolorem ipsum quia dolor.</p>
<div class="abs read-more" style="top:1973px">READ MORE</div>

<div class="abs post-img" style="top:2070px;background:linear-gradient(135deg,#d8d2c8,#8a8a8a 50%,#3a3a3e)" role="img" aria-label="Photograph of a hand holding a phone above a keyboard with digital icons"></div>
<h3 class="abs post-title" style="top:2065px">Sed ut perspiciatis unde omnis iste natus sit vieol uptatem accusantium dolorem</h3>
<div class="abs meta post-meta" style="top:2159px">
  <svg width="13" height="13" viewBox="0 0 13 13"><rect x="0.5" y="1.5" width="12" height="11" fill="none" stroke="#ec1f27" stroke-width="1.4"/><rect x="0.5" y="1.5" width="12" height="3" fill="#ec1f27"/></svg>18/03/2019<span class="sep">|</span>
  <svg width="12" height="13" viewBox="0 0 12 13"><circle cx="6" cy="3.5" r="3" fill="#ec1f27"/><path d="M0 13 Q0 7 6 7 Q12 7 12 13Z" fill="#ec1f27"/></svg>John Doe
</div>
<p class="abs post-text" style="top:2201px">Nemo enim ipsam voluptatem quia voluptas sit aspernatur aut odit aut fugit, sed quia consequuntur magni dolores eos qui ratione voluptatem sequi nesciuntu po rro quisquam est, qui dolorem ipsum quia dolor.</p>
<div class="abs read-more" style="top:2316px">READ MORE</div>

<div class="abs post-img" style="top:2414px;background:linear-gradient(135deg,#5a3a22,#9a7250 50%,#4a2e1a)" role="img" aria-label="Photograph of people working with a laptop and phones on a wooden desk"></div>
<h3 class="abs post-title" style="top:2408px">Sed ut perspiciatis unde omnis iste natus sit vieol uptatem accusantium dolorem</h3>
<div class="abs meta post-meta" style="top:2502px">
  <svg width="13" height="13" viewBox="0 0 13 13"><rect x="0.5" y="1.5" width="12" height="11" fill="none" stroke="#ec1f27" stroke-width="1.4"/><rect x="0.5" y="1.5" width="12" height="3" fill="#ec1f27"/></svg>18/03/2019<span class="sep">|</span>
  <svg width="12" height="13" viewBox="0 0 12 13"><circle cx="6" cy="3.5" r="3" fill="#ec1f27"/><path d="M0 13 Q0 7 6 7 Q12 7 12 13Z" fill="#ec1f27"/></svg>John Doe
</div>
<p class="abs post-text" style="top:2544px">Nemo enim ipsam voluptatem quia voluptas sit aspernatur aut odit aut fugit, sed quia consequuntur magni dolores eos qui ratione voluptatem sequi nesciuntu po rro quisquam est, qui dolorem ipsum quia dolor.</p>
<div class="abs read-more" style="top:2659px">READ MORE</div>

<div class="abs view-more">VIEW MORE</div>

<!-- podcast -->
<h2 class="abs section-title" style="top:3017px">PODCAST</h2>
<div class="abs round-arrow" style="left:36px"><svg width="14" height="14" viewBox="0 0 14 14"><polyline points="9,2 4,7 9,12" fill="none" stroke="#666" stroke-width="2"/></svg></div>
<div class="abs round-arrow" style="left:1124px"><svg width="14" height="14" viewBox="0 0 14 14"><polyline points="5,2 10,7 5,12" fill="none" stroke="#666" stroke-width="2"/></svg></div>

<div class="abs cast-img" style="left:113px" role="img" aria-label="Video still of two people in conversation">
  <div class="abs play"><svg width="20" height="22" viewBox="0 0 20 22"><polygon points="3,1 19,11 3,21" fill="#111"/></svg></div>
</div>
<div class="abs cast-img" style="left:445px;background:linear-gradient(135deg,#2a2a2e,#8a6a4a 55%,#1e1e22)" role="img" aria-label="Video still of hands holding a smartphone">
  <div class="abs play"><svg width="20" height="22" viewBox="0 0 20 22"><polygon points="3,1 19,11 3,21" fill="#111"/></svg></div>
</div>
<div class="abs cast-img" style="left:780px;background:linear-gradient(135deg,#1a2430,#4a5a70 50%,#6a5a4a)" role="img" aria-label="Video still of a person using a phone among city lights">
  <div class="abs play"><svg width="20" height="22" viewBox="0 0 20 22"><polygon points="3,1 19,11 3,21" fill="#111"/></svg></div>
</div>

<h3 class="abs cast-title" style="left:113px">Nemo enim ipsam voluptatem quia voluptas sit aspernatur au</h3>
<h3 class="abs cast-title" style="left:445px">Nemo enim ipsam voluptatem quia voluptas sit aspernatur au</h3>
<h3 class="abs cast-title" style="left:780px">Nemo enim ipsam voluptatem quia voluptas sit aspernatur au</h3>
<div class="abs meta cast-meta" style="left:113px">
  <svg width="13" height="13" viewBox="0 0 13 13"><rect x="0.5" y="1.5" width="12" height="11" fill="none" stroke="#ec1f27" stroke-width="1.4"/><rect x="0.5" y="1.5" width="12" height="3" fill="#ec1f27"/></svg>18/03/2019<span class="sep">|</span>
  <svg width="12" height="13" viewBox="0 0 12 13"><circle cx="6" cy="3.5" r="3" fill="#ec1f27"/><path d="M0 13 Q0 7 6 7 Q12 7 12 13Z" fill="#ec1f27"/></svg>John Doe
</div>
<div class="abs meta cast-meta" style="left:445px">
  <svg width="13" height="13" viewBox="0 0 13 13"><rect x="0.5" y="1.5" width="12" height="11" fill="none" stroke="#ec1f27" stroke-width="1.4"/><rect x="0.5" y="1.5" width="12" height="3" fill="#ec1f27"/></svg>18/03/2019<span class="sep">|</span>
  <svg width="12" height="13" viewBox="0 0 12 13"><circle cx="6" cy="3.5" r="3" fill="#ec1f27"/><path d="M0 13 Q0 7 6 7 Q12 7 12 13Z" fill="#ec1f27"/></svg>John Doe
</div>
<div class="abs meta cast-meta" style="left:780px">
  <svg width="13" height="13" viewBox="0 0 13 13"><rect x="0.5" y="1.5" width="12" height="11" fill="none" stroke="#ec1f27" stroke-width="1.4"/><rect x="0.5" y="1.5" width="12" height="3" fill="#ec1f27"/></svg>18/03/2019<span class="sep">|</span>
  <svg width="12" height="13" viewBox="0 0 12 13"><circle cx="6" cy="3.5" r="3" fill="#ec1f27"/><path d="M0 13 Q0 7 6 7 Q12 7 12 13Z" fill="#ec1f27"/></svg>John Doe
</div>

<!-- quote -->
<div class="abs quote-band"></div>
<div class="abs quote-badge">
  <svg width="46" height="36" viewBox="0 0 46 36"><path d="M2 36V20Q2 4 18 0L20 6Q10 9 10 18H18V36Z M26 36V20Q26 4 42 0L44 6Q34 9 34 18H42V36Z" fill="#ec1f27"/></svg>
</div>
<p class="abs quote-text">“ Nemo enim ipsam voluptatem quia voluptas sit aspernatur aut odit aut fugit, sed quia consequ untur magni dolores”</p>
<p class="abs quote-name">— MARCUS DELANE</p>

<!-- footer -->
<div class="abs social" style="left:488px"></div>
<div class="abs social" style="left:547px"></div>
<div class="abs social" style="left:606px"></div>
<div class="abs social" style="left:665px"></div>
<div class="abs contact">
  <svg width="11" height="15" viewBox="0 0 11 15"><path d="M5.5 0A5.5 5.5 0 0 0 0 5.5C0 9.5 5.5 15 5.5 15S11 9.5 11 5.5A5.5 5.5 0 0 0 5.5 0Z" fill="#ec1f27"/><circle cx="5.5" cy="5.5" r="2" fill="#fff"/></svg>
  <span>1480 Harbor Lane Suite 210 Portland, Oregon 97201</span><span>|</span>
  <svg width="14" height="14" viewBox="0 0 14 14"><path d="M3 0L5.5 3.5 4 5.5Q5.5 8.5 8.5 10L10.5 8.5 14 11 12 14Q5 13 0 2Z" fill="#ec1f27"/></svg>
  <span>1 800 555 0142</span><span>|</span>
  <svg width="16" height="12" viewBox="0 0 16 12"><rect width="16" height="12" fill="#ec1f27"/><polyline points="0,0 8,7 16,0" fill="none" stroke="#fff" stroke-width="1.4"/></svg>
  <span>info@brightlatticehub.tv</span>
</div>
<p class="abs links">Help<span class="bar">|</span>FAQ<span class="bar">|</span>Support<span class="bar">|</span>Sitemap<span class="bar">|</span>Terms Of Use<span class="bar">|</span>Privacy Statement</p>
<p class="abs copyright">Bright Lattice Hub © 2019 All rights reserved.</p>

</body>
</html>
```